'Wedding Business" Business Card Design

dj services for weddings and parties, uplighting, event planning, day of coordination for weddings, photography for weddings and other events.

Would like raised print and metallic also if possible. Elegant design, yet modern. This is a wedding business and should describe our goals and main services - DJ/lighting, wedding and event planning, photography. slogan "Simply Incredible, Incredibly simple" or "Your Dreams. Our Experience. The Perfect Match" Our goal is to provide multiple services to make it easier for the bride and groom almost like a one stop shop. Feel free to use the slogan or leave it out , we just want to really stand out against the competition. You can also get more info on our website www.bluelarkproductions.com - we are working to get the bluelarkct.com site pointed to our current site!

there should be 2 files attached, if they did not go through please email events@bluelarkct.com or bluelarkproductions@mailbox.test
Updates

Thank you all for your help, we have decided what we like but would like to make some changes, we need to order these asap so please let us know if you can help.

Reason: Wasn't able to pick it out in time! So Sorry but we know what we want!!

Industry/Entity Type

Business

Contact Information for Business Card

Trevor and Mallory Quenby
555-318-2746
555-207-4831
Blue Lark Productions, Events, & Photography
EMAIL:Events@BlueLarkCT.com
www.bluelarkct.com

```html
<!DOCTYPE html>
<html lang="en">
<head>
<meta charset="utf-8">
<title>Blue Lark Productions – Business Card</title>
<link rel="stylesheet" href="https://fonts.googleapis.com/css2?family=Montserrat:wght@400;500&display=swap">
<style>
  :root {
    --backdrop: #e6e6e6;
    --card: #000000;
    --silver: #c8c8d4;
    --white: #ffffff;
    --rule: #bdbdbd;
    --icon-blue: #3a3fa8;
  }
  * { margin: 0; padding: 0; box-sizing: border-box; }
  html, body { width: 1000px; height: 1200px; overflow: hidden; }
  body {
    background: var(--backdrop);
    font-family: "Montserrat", Arial, sans-serif;
    position: relative;
  }
  .card {
    position: absolute;
    width: 699px;
    height: 409px;
    background: var(--card);
    color: var(--white);
  }
  .card--front { left: 141px; top: 102px; }
  .card--back { left: 141px; top: 658px; }

  .wordmark {
    position: absolute;
    color: var(--silver);
    font-weight: 400;
    text-align: center;
    line-height: 1;
    letter-spacing: 0.04em;
  }
  .card--front .wordmark {
    left: 0; right: 0; top: 145px;
    font-size: 52px;
  }
  .card--front .wordmark span { display: block; margin-bottom: 14px; }
  .card--back .wordmark {
    left: 478px; width: 120px; top: 62px;
    font-size: 26px;
  }
  .card--back .wordmark span { display: block; margin-bottom: 8px; }

  .owner-name {
    position: absolute;
    left: 58px; top: 211px;
    font-size: 16.5px;
    font-weight: 500;
    letter-spacing: 0.03em;
    white-space: nowrap;
  }
  .owner-rule {
    position: absolute;
    left: 306px; top: 225px;
    width: 341px; height: 1px;
    background: var(--rule);
  }
  .contact-list {
    position: absolute;
    left: 62px; top: 264px;
    list-style: none;
    font-size: 11.5px;
    letter-spacing: 0.03em;
  }
  .contact-list li {
    display: flex;
    align-items: center;
    height: 22px;
  }
  .contact-list svg {
    width: 13px; height: 13px;
    margin-right: 11px;
    flex: none;
  }
  .company-lines {
    position: absolute;
    left: 440px; width: 200px; top: 283px;
    font-size: 11.5px;
    line-height: 22px;
    text-align: center;
    letter-spacing: 0.02em;
  }
</style>
</head>
<body>

<section class="card card--front">
  <div class="wordmark"><span>Blue</span><span>Lark</span></div>
</section>

<section class="card card--back">
  <div class="wordmark"><span>Blue</span><span>Lark</span></div>

  <p class="owner-name">Trevor and Mallory Quenby</p>
  <div class="owner-rule"></div>

  <ul class="contact-list">
    <li>
      <svg viewBox="0 0 13 13" aria-hidden="true">
        <rect width="13" height="13" fill="var(--icon-blue)"/>
        <path d="M6.5 3 L10 6.3 H9 V10 H4 V6.3 H3 Z" fill="#fff"/>
      </svg>
      555-318-2746 /555-207-4831
    </li>
    <li>
      <svg viewBox="0 0 13 13" aria-hidden="true">
        <rect width="13" height="13" fill="var(--icon-blue)"/>
        <path d="M4 3.2 L5.6 3 L6.2 5 L5.3 5.7 Q6 7.2 7.3 7.8 L8 6.9 L10 7.5 L9.8 9.1 Q6.5 9.5 4.5 7 Q3.3 5.3 4 3.2 Z" fill="#fff"/>
      </svg>
      :Events@BlueLarkCT.com
    </li>
    <li>
      <svg viewBox="0 0 13 13" aria-hidden="true">
        <rect width="13" height="13" fill="var(--icon-blue)"/>
        <circle cx="6.5" cy="6.5" r="2.6" fill="none" stroke="#fff" stroke-width="1"/>
      </svg>
      www.bluelarkct.com
    </li>
  </ul>

  <div class="company-lines">
    <p>Blue Lark Productions</p>
    <p>Events, &amp; Photography</p>
  </div>
</section>

</body>
</html>
```